Stellan App | Pre-Launch Homepage

Dear designer,
Stellan is a soon to be launched innovative & free social platform for collaborative addictions quitting.
We require a design for our pre-launch homepage that will elevate our basic wireframes to the next level.
We would like the wireframes to serve as a guideline only, and not as a final version of the design. If you have cool ideas - we would appreciate your creativity!
* This is a pre-launch website for a mobile app, and as such the design must be consistent with the general style, design and atmosphere of the app (see screenshot in the shared Drive link).
* We liked the style and feel of the following website: http://plumvane.com/ - Please let's use it as a reference as well.
* The existing text in the wireframes is there just to represent a place for text. Copy will be edited by us after the design is done.
Please find the wireframes attached, and all relevant design assets and app screenshots in the following Drive shared link -
https://files.orbelink.com/open?id=7K204XqR3tPmHc8Lw2Jd61VnaGzT
Thanks,
Marcus
Industry/Entity Type
Social
Number of Pages Required
1 page
Look and feel
Each slider illustrates characteristics of the customer's brand and the style your logo design should communicate.

```html
<!DOCTYPE html>
<html lang="en">
<head>
<meta charset="utf-8">
<title>Stellan | Become a Better Version of Yourself</title>
<link rel="stylesheet" href="https://fonts.googleapis.com/css2?family=Raleway:wght@300;400;500;600;700&display=swap">
<style>
  :root {
    --orange: #f7941d;
    --orange-deep: #e8780f;
    --orange-light: #fbb040;
    --ink: #333333;
    --muted: #777777;
    --hero-dark: #232323;
    --hero-brown: #3d2c1f;
    --fun-brown: #4e3424;
    --fun-brown-dark: #2f2018;
    --paper: #ffffff;
    --mist: #f1f1f1;
    --line: #d9d9d9;
    --device: #1c1c1c;
    --screen: #3b4a5a;
  }
  * { box-sizing: border-box; margin: 0; padding: 0; }
  html, body { width: 1200px; height: 3980px; overflow: hidden; }
  body { font-family: "Raleway", sans-serif; color: var(--ink); background: var(--paper); position: relative; }
  section, footer { position: absolute; left: 0; width: 1200px; }
  .abs { position: absolute; }
  .btn { display: inline-block; background: var(--orange); color: #fff; font-weight: 600; font-size: 13px; text-transform: uppercase; letter-spacing: .5px; border-radius: 4px; text-align: center; }
  .chevron { position: absolute; left: 575px; width: 50px; height: 50px; border-radius: 50%; background: var(--paper); box-shadow: 0 2px 6px rgba(0,0,0,.15); z-index: 5; }
  .chevron svg { position: absolute; left: 15px; top: 17px; }
  .device { background: var(--device); border-radius: 22px; }
  .screen { position: absolute; background: linear-gradient(160deg, var(--screen), #1f2a35); border-radius: 4px; }

  /* hero */
  .hero { top: 0; height: 660px; background: radial-gradient(ellipse at 50% 40%, var(--hero-brown), var(--hero-dark) 70%); color: #fff; text-align: center; }
  .brand { font-weight: 700; color: var(--orange); font-size: 56px; letter-spacing: 1px; }
  .hero .brand { position: absolute; top: 22px; left: 0; width: 100%; }
  .contact-btn { position: absolute; top: 22px; left: 924px; width: 176px; height: 46px; line-height: 46px; border-radius: 23px; border: 2px solid #fff; font-size: 15px; text-transform: none; }
  .tagline { position: absolute; top: 116px; width: 100%; font-size: 26px; color: var(--orange); font-weight: 400; }
  .intro { position: absolute; top: 170px; left: 380px; width: 440px; font-size: 15px; line-height: 1.6; color: #ddd; }
  .subscribe-box { position: absolute; top: 246px; left: 380px; width: 440px; height: 150px; background: rgba(0,0,0,.55); padding: 26px 30px; }
  .subscribe-box h2 { font-weight: 400; font-size: 20px; line-height: 1.35; color: #fff; }
  .field { display: flex; height: 40px; margin-top: 20px; background: #fff; border-radius: 3px; padding: 5px; }
  .field span.placeholder { flex: 1; text-align: left; color: #999; font-size: 12px; line-height: 30px; padding-left: 10px; }
  .field .btn { width: 110px; line-height: 30px; font-size: 11px; }
  .hero-tablet { left: 20px; top: 270px; width: 220px; height: 300px; transform: rotate(-8deg); }
  .hero-phone { left: 870px; top: 170px; width: 210px; height: 420px; transform: rotate(10deg); border-radius: 30px; }
  .mini-devices { left: 520px; top: 412px; width: 160px; height: 50px; }

  /* features */
  .features { top: 660px; height: 380px; background: var(--mist); }
  .feature { position: absolute; top: 60px; width: 260px; height: 260px; text-align: center; padding-top: 30px; }
  .feature.is-active { background: var(--paper); box-shadow: 0 2px 10px rgba(0,0,0,.08); }
  .feature-icon { width: 120px; height: 120px; margin: 0 auto; border-radius: 50%; border: 4px solid var(--orange); background: var(--paper); display: flex; align-items: center; justify-content: center; }
  .feature h3 { margin-top: 22px; font-size: 22px; font-weight: 400; }
  .feature p { margin-top: 8px; font-size: 12px; color: var(--muted); line-height: 1.5; padding: 0 30px; }

  /* fun */
  .fun { top: 1020px; height: 420px; background: linear-gradient(135deg, var(--fun-brown), var(--fun-brown-dark)); clip-path: polygon(0 40px, 100% 0, 100% 100%, 0 100%); color: #fff; }
  .section-title { font-weight: 300; font-size: 56px; }
  .fun .section-title { position: absolute; left: 700px; top: 100px; }
  .body-copy { font-size: 14px; line-height: 1.7; }
  .body-copy p + p { margin-top: 16px; }
  .fun .body-copy { position: absolute; left: 700px; top: 190px; width: 420px; color: #e6d8cc; }
  .body-copy strong { color: var(--orange); font-weight: 700; }
  .fun-tablet { left: 70px; top: 100px; width: 500px; height: 300px; transform: rotate(-6deg); border-radius: 26px; }

  /* inspire */
  .inspire { top: 1420px; height: 420px; background: linear-gradient(120deg, var(--orange-light), var(--orange) 45%, var(--orange-deep)); color: #fff; }
  .inspire .section-title { position: absolute; left: 80px; top: 110px; }
  .inspire .body-copy { position: absolute; left: 80px; top: 200px; width: 420px; }
  .inspire .body-copy strong { color: var(--fun-brown); }
  .inspire-tablet { left: 640px; top: 60px; width: 500px; height: 290px; transform: rotate(-12deg); border-radius: 26px; background: #e9e9e9; }

  /* achieve */
  .achieve { top: 1840px; height: 600px; background: var(--paper); text-align: center; }
  .achieve .section-title { position: absolute; top: 60px; width: 100%; color: var(--ink); }
  .achieve .lead { position: absolute; top: 150px; left: 340px; width: 520px; font-size: 14px; line-height: 1.6; color: var(--muted); }
  .achieve .lead strong { color: var(--orange); }
  .achieve .motto { position: absolute; top: 220px; width: 100%; font-size: 14px; color: var(--muted); }
  .achieve-phone { left: 510px; top: 270px; width: 180px; height: 340px; border-radius: 28px 28px 0 0; }
  .point { position: absolute; width: 200px; font-size: 12px; line-height: 1.5; color: var(--muted); }
  .point.left { text-align: right; }
  .point.right { text-align: left; }
  .point-icon { position: absolute; width: 60px; height: 60px; border-radius: 50%; border: 3px solid var(--orange); background: var(--paper); display: flex; align-items: center; justify-content: center; }
  .connector { position: absolute; height: 1px; background: var(--line); }

  /* coming soon */
  .coming { top: 2440px; height: 540px; background: linear-gradient(150deg, var(--orange-light), var(--orange) 50%, var(--orange-deep)); text-align: center; color: #fff; }
  .coming .section-title { position: absolute; top: 70px; width: 100%; }
  .coming-phone { left: 520px; top: 170px; width: 170px; height: 340px; border-radius: 28px; }
  .earphones { left: 380px; top: 460px; width: 440px; height: 60px; }

  /* download */
  .download { top: 2980px; height: 400px; background: var(--paper); text-align: center; }
  .download h2 { position: absolute; top: 130px; width: 100%; font-weight: 400; font-size: 40px; }
  .download .sub { position: absolute; top: 195px; width: 100%; font-size: 13px; color: var(--muted); }
  .store { position: absolute; top: 312px; width: 230px; height: 54px; border: 2px solid var(--line); border-radius: 27px; display: flex; align-items: center; justify-content: center; gap: 12px; font-size: 17px; color: var(--muted); }
  .store.is-primary { border-color: var(--orange); color: var(--orange); }
  .store i { width: 22px; height: 22px; border-radius: 50%; background: currentColor; display: block; }

  /* newsletter */
  .newsletter { top: 3380px; height: 240px; background: var(--mist); text-align: center; }
  .newsletter h2 { position: absolute; top: 70px; width: 100%; font-weight: 400; font-size: 28px; }
  .newsletter .sub { position: absolute; top: 112px; width: 100%; font-size: 12px; color: var(--muted); }
  .newsletter .field { position: absolute; top: 150px; left: 340px; width: 520px; margin: 0; border: 1px solid var(--line); }

  /* footer */
  .site-footer { top: 3620px; height: 360px; background: var(--orange); text-align: center; color: #fff; }
  .footer-tab { position: absolute; left: 80px; top: -20px; width: 60px; height: 20px; background: var(--orange); clip-path: polygon(20% 0, 80% 0, 100% 100%, 0 100%); }
  .site-footer .brand { position: absolute; top: 70px; width: 100%; color: #fff; font-size: 50px; }
  .footer-links { position: absolute; top: 160px; width: 100%; font-size: 14px; }
  .footer-links a { color: #fff; text-decoration: none; margin: 0 18px; }
  .socials { position: absolute; top: 220px; left: 0; width: 100%; display: flex; justify-content: center; gap: 24px; }
  .socials span { width: 48px; height: 48px; border-radius: 50%; border: 2px solid #fff; }
  .copyright { position: absolute; top: 315px; width: 100%; font-size: 12px; color: #fde2c0; }
</style>
</head>
<body>

<section class="hero">
  <div class="brand">Stellan</div>
  <a class="btn contact-btn">Contact Us</a>
  <h1 class="tagline">Become a Better Version of Yourself</h1>
  <p class="intro">Stellan is a revolutionary &amp; free social platform for collaborative addictions quitting.</p>
  <div class="abs device hero-tablet" role="img" aria-label="Tablet showing the Stellan app home screen"><div class="screen" style="left:14px;top:18px;right:14px;bottom:18px"></div></div>
  <div class="subscribe-box">
    <h2>Subscribe below for the beta release and updates.</h2>
    <div class="field"><span class="placeholder">Enter your email address</span><span class="btn">Let me know!</span></div>
  </div>
  <div class="abs mini-devices" role="img" aria-label="Small row of phone and tablet devices" style="background:linear-gradient(90deg,#555,#888,#555);border-radius:6px"></div>
  <div class="abs device hero-phone" role="img" aria-label="Phone showing the Stellan app profile screen"><div class="screen" style="left:12px;top:50px;right:12px;bottom:50px"></div></div>
</section>
<div class="chevron" style="top:635px"><svg width="20" height="14" viewBox="0 0 20 14"><path d="M2 3 L10 11 L18 3" fill="none" stroke="#777" stroke-width="2.5"/></svg></div>

<section class="features">
  <div class="feature is-active" style="left:170px">
    <div class="feature-icon"><svg width="64" height="64" viewBox="0 0 64 64"><circle cx="32" cy="32" r="26" fill="none" stroke="#e84b3a" stroke-width="12"/><circle cx="32" cy="32" r="26" fill="none" stroke="#fff" stroke-width="12" stroke-dasharray="14 27"/></svg></div>
    <h3>Never be Alone</h3>
    <p>Forget what you know - Stellan makes it fun to quit.</p>
  </div>
  <div class="feature" style="left:470px">
    <div class="feature-icon"><svg width="64" height="64" viewBox="0 0 64 64"><path d="M32 4 L40 24 L62 25 L45 39 L51 60 L32 48 L13 60 L19 39 L2 25 L24 24 Z" fill="#f5b928"/></svg></div>
    <h3>Network Power</h3>
    <p>Forget what you know - Stellan makes it fun to quit.</p>
  </div>
  <div class="feature" style="left:770px">
    <div class="feature-icon"><svg width="64" height="64" viewBox="0 0 64 64"><circle cx="32" cy="32" r="22" fill="none" stroke="#666" stroke-width="10" stroke-dasharray="8 6"/><circle cx="32" cy="32" r="12" fill="#888"/></svg></div>
    <h3>Stay Motivated</h3>
    <p>Forget what you know - Stellan makes it fun to quit.</p>
  </div>
</section>

<section class="fun">
  <div class="abs device fun-tablet" role="img" aria-label="Tablet showing the Stellan campaign battle screen"><div class="screen" style="left:30px;top:20px;right:30px;bottom:20px"></div></div>
  <h2 class="section-title">Fun</h2>
  <div class="body-copy">
    <p>Forget what you know - <strong>Stellan makes it fun to quit.</strong> The battle between your good and bad demons comes to life in our <strong>gamified approach</strong> for managing your campaigns.</p>
    <p>Stellan gives you the opportunity to take an <strong>active role</strong> in helping your network to <strong>smash</strong> your common addictions as a team. That's right, we converted the cessation process into a social game.</p>
  </div>
</section>

<section class="inspire">
  <h2 class="section-title">Inspire</h2>
  <div class="body-copy">
    <p>One of the most important factors for successful quitting is the ability to <strong>stay inspired</strong> during the process.</p>
    <p>That's why we designed Stellan as a platform where you can inspire and be inspired by a supportive network of passionate quitters.</p>
  </div>
  <div class="abs device inspire-tablet" role="img" aria-label="White tablet showing the Stellan inspiration feed"><div class="screen" style="left:30px;top:20px;right:30px;bottom:20px"></div></div>
</section>
<div class="chevron" style="top:1815px"><svg width="20" height="14" viewBox="0 0 20 14"><path d="M2 3 L10 11 L18 3" fill="none" stroke="#777" stroke-width="2.5"/></svg></div>

<section class="achieve">
  <h2 class="section-title">Achieve</h2>
  <p class="lead">Stellan is built as a <strong>pyramid of relationships</strong> that makes use of the <strong>Social Cognitive Theory</strong>, to provide a powerful network of positive reinforcement.</p>
  <p class="motto">The bigger you make it the stronger you get.</p>

  <p class="point left" style="left:130px;top:340px">Stellan is built as a pyramid of relationships that makes use of the Social Cognitive Theory.</p>
  <div class="connector" style="left:340px;top:367px;width:30px"></div>
  <div class="point-icon" style="left:370px;top:337px"><svg width="30" height="30" viewBox="0 0 30 30"><circle cx="15" cy="15" r="12" fill="#4a7fb5"/></svg></div>
  <p class="point left" style="left:130px;top:510px">Stellan is built as a pyramid of relationships that makes use of the Social Cognitive Theory.</p>
  <div class="connector" style="left:340px;top:537px;width:30px"></div>
  <div class="point-icon" style="left:370px;top:507px"><svg width="30" height="30" viewBox="0 0 30 30"><rect x="6" y="6" width="18" height="18" rx="9" fill="none" stroke="#777" stroke-width="4"/></svg></div>

  <div class="point-icon" style="left:770px;top:337px"><svg width="30" height="30" viewBox="0 0 30 30"><path d="M8 5 H22 V12 A7 7 0 0 1 8 12 Z M13 19 H17 V23 H21 V26 H9 V23 H13 Z" fill="#555"/></svg></div>
  <div class="connector" style="left:830px;top:367px;width:30px"></div>
  <p class="point right" style="left:870px;top:340px">Stellan is built as a pyramid of relationships that makes use of the Social Cognitive Theory.</p>
  <div class="point-icon" style="left:770px;top:507px"><svg width="30" height="30" viewBox="0 0 30 30"><path d="M4 10 H26 L23 25 H7 Z" fill="none" stroke="#555" stroke-width="2.5"/></svg></div>
  <div class="connector" style="left:830px;top:537px;width:30px"></div>
  <p class="point right" style="left:870px;top:510px">Stellan is built as a pyramid of relationships that makes use of the Social Cognitive Theory.</p>

  <div class="abs device achieve-phone" role="img" aria-label="Phone showing a Stellan user profile with progress bars"><div class="screen" style="left:12px;top:46px;right:12px;bottom:0"></div></div>
</section>

<section class="coming">
  <h2 class="section-title">Coming Soon</h2>
  <svg class="abs" style="left:300px;top:330px" width="600" height="160" viewBox="0 0 600 160">
    <path d="M200 20 Q60 40 40 140" fill="none" stroke="#fff" stroke-width="2"/>
    <path d="M30 125 L40 142 L52 128" fill="none" stroke="#fff" stroke-width="2"/>
    <path d="M400 20 Q540 40 560 140" fill="none" stroke="#fff" stroke-width="2"/>
    <path d="M548 128 L560 142 L570 125" fill="none" stroke="#fff" stroke-width="2"/>
  </svg>
  <div class="abs device coming-phone" role="img" aria-label="Phone showing the Stellan app profile screen"><div class="screen" style="left:11px;top:46px;right:11px;bottom:46px"></div></div>
  <div class="abs earphones" role="img" aria-label="White earphones lying beside the phone" style="background:radial-gradient(ellipse at center,rgba(255,255,255,.7),rgba(255,255,255,0) 70%)"></div>
</section>

<section class="download">
  <h2>Download Our App</h2>
  <p class="sub">Choose your native platform and download the app.</p>
  <div class="store is-primary" style="left:208px"><i></i>Playfield</div>
  <div class="store" style="left:485px"><i></i>Appvault</div>
  <div class="store" style="left:762px"><i></i>Paneshop</div>
</section>

<section class="newsletter">
  <h2>Subscribe To Newsletter</h2>
  <p class="sub">Subscribe below for the beta release and updates.</p>
  <div class="field"><span class="placeholder">Enter your email address</span><span class="btn">Let me know!</span></div>
</section>

<footer class="site-footer">
  <div class="footer-tab"></div>
  <div class="brand">Stellan</div>
  <nav class="footer-links"><a>About Us</a><a>T&amp;Cs</a><a>Privacy Policy</a></nav>
  <div class="socials"><span></span><span></span><span></span></div>
  <p class="copyright">© 2015 Stellan Inc. All Rights Reserved.</p>
</footer>

</body>
</html>
```